KTV - GENERAL DATA PROTECTION REGULATION

Our network of companies is called : KTV (KTVR-QLM FLARES).
It is sourced and based in Brussels, Belgium, hosting the EU institutions : designers and enforcers of the GDPR (https://portal.vendrimatex.example/info/rules/privacy-notes_en).
We are setting up connected, empowered and visionary-interconnected organizations in each country, region or city concerned by the GDPR.
We have developed unique pedagogical methods, programs, instruments (video, softwares,…) and visionary training skills – initially and on a continuous basis – for the DPO & GDPR consultants.
Our motto is : From Challenges to Opportunities.
Our yearning is : developing soulful teams, join forces & talents with our clients.
Our most wanted reward : let us astonish you!
We opt for the best available softwares on the market for project management, data analytics, GDPR compliance, DPO assistance and in general : customer relation and enhanced communication between project members.
We contribute to bringing Artificial Intelligence and Data-Driven Mindsets in enterprises.
We perceive the GDPR as the best opportunity an organization faces to value its “gold” (its data) and offer the solutions to transform them into real-life currencies and assets… MONEY .
I guess my comments need time to be integrated and I provided a lot of text too! I would particularly encourage RT (UK) to take the best out of his several proposals to mix them in the best ONE website! Offering me many graphic elements to use for all my posts/pages... I am a prolix writer :)
Target Market(s)
SME's business leaders, HR and Legal departments, read : https://www.kovalnews.example/article/us-privacy-role/growth-of-the-privacy-lead-the-newest-job-in-demand-idUSKQ7ZT4PL
Industry/Entity Type
Legal
Coding
Coded - Design and coding required
Number of Pages Required
5+ page
Colors
Designer to choose colors to be used in the design.
Requirements
Must have
- A HUMAN APPROACH
- WE NEED TO SEE HUMANS AND NOT ONLY ROBOTS OR ELECTRONIC DEVICES.
- 1) The DPO/GDPR Logos of the companies:
- https://www.filtrunbox.example/sh/k82r44tbzq7nn22/BBD4maPeFhBy1pllrk5Gnnqb?dl=0
- https://www.filtrunbox.example/sh/q3x71fjzr55kzd/BBB9bjVFdde_p8mnpuBzRgs?dl=0 et DPO : https://www.filtrunbox.example/sh/t6v9k3dtp44zz7q/BBEjuYFfMvuwtxnECRC6LnmTR-b?dl=0
- OR :
- https://www.filtrunbox.example/sh/wemmdv2jr5kbzw/BBBSeYNPFeWmNEWCLO3RSg3qWb?dl=0
- AND :
- https://stewardlane.teamvault.example/sites/all/_layouts/15/guestaccess.aspx?guestaccesstoken=K4bbqw862NMTW7KhcM4Wq0p%2BScqNwdl1sqQk%2FmUmQOV%3D&folderid=2_3f71b91a29a805d81c96b8636e419f7ce&rev=1&e=6b611bf144535597b9296c99cd6116c9
- 2) A surprising but human, clear, simple, white, lightning look!
- 3) WORDPRESS version so that I can edit easily and add text on existing and new pages
- We therefore pass each option and - even more so - through the sieve of this inevitable - and values-generating - ethical evaluation.
- In other words, we are doubly satisfied with EVERY solution:
- 1. As a DPO/consultant and advisor to commercial enterprises or non-profit organisations but necessarily entering into a relationship involving financial flows with the persons concerned; and
- 2. As concerned person: target of the actions envisaged, parent, child, citizen and avatar in our digital lives.
- We put personal data at the centre of our projects and internal meetings, and with clients, we therefore continue the stage of brainstorming, researching and visualising ideas in interaction with the Regulation, by analysing the ethical consequences of each option.
- We choose only solutions that are applicable to the greatest number and therefore satisfy us as citizens of an increasingly connected and digital world. We also see the Regulation as a commercial and marketing opportunity to enhance the value of personal data and develop the confidence of those concerned by respect and security in the processing of such data.
- Our ultimate test: we put ourselves in our children's shoes to test the option considered, then comment on it and evaluate it as a parent.
- NO TO INCOMPREHENSIVE LEGAL TERMS... It is simply prohibited from 25 May for all information to be communicated to the persons concerned by the Regulation!
Nice to have
- - Artificial Intelligence
- - Transhumans
- - Challenges becoming Opportunities
- - a Great Dame who Protects & Reassures (see GDPR logo)
- - Friendly communication - NOT too businesslike/cold/usual
- - Page content is available here in FRENCH then ENGLISH then DUTCH then GERMAN : https://www.filtrunbox.example/sh/r1hgqmzsa101zwv/BBDNSzNQSFzz2qvvIZr5Ca?dl=0
Should not have
- A cold, bankerlike, old economy, dull outlook

```html
<!DOCTYPE html>
<html lang="en">
<head>
<meta charset="utf-8">
<title>KTV — GDPR &amp; DPO</title>
<link href="https://fonts.googleapis.com/css2?family=Poppins:wght@400;500;600&display=swap" rel="stylesheet">
<style>
:root{
  --navy:#0b1a8f;
  --blue:#2a3fae;
  --yellow:#ffe014;
  --ink:#1b2166;
  --slate:#9ba6b1;
  --slate-dark:#6e7a87;
  --footer:#263242;
  --footer-text:#9aa6b4;
  --white:#ffffff;
  --page:#e9eaec;
}
*{margin:0;padding:0;box-sizing:border-box}
html,body{width:738px;height:1200px;overflow:hidden;background:var(--page)}
body{font-family:"Poppins",sans-serif;color:var(--ink)}
.page{position:relative;width:738px;height:1200px;overflow:hidden;background:var(--white)}
section,footer{position:absolute;left:0;width:738px;overflow:hidden}

/* hero */
.hero{top:0;height:320px}
.hero-photo{position:absolute;inset:0;background:linear-gradient(110deg,#f6f8fb 0%,#eef1f6 45%,#d9dde4 75%,#b9bec8 100%)}
.brand{position:absolute;left:34px;top:24px;display:flex;align-items:center;gap:8px}
.brand-dot{width:22px;height:22px;border-radius:50%;background:var(--yellow)}
.brand-name{font-size:22px;font-weight:600;color:var(--navy);letter-spacing:1px}
.nav{position:absolute;top:32px;left:0;width:100%}
.nav a{position:absolute;font-size:7px;font-weight:500;color:var(--navy);text-decoration:none;letter-spacing:.3px}
.nav a.is-active{border-bottom:1px solid var(--yellow);padding-bottom:3px}
.nav .btn-contact{left:627px;top:-7px;width:86px;height:22px;background:var(--yellow);display:flex;align-items:center;justify-content:center}
.hero-copy{position:absolute;left:84px;top:170px;font-size:17px;font-weight:400;line-height:22px;color:var(--navy);width:360px}
.hero-copy strong{font-weight:600}
.btn-outline{display:inline-block;font-size:7px;font-weight:500;letter-spacing:.3px;text-decoration:none;padding:6px 14px;border:1px solid currentColor}
.hero .btn-outline{position:absolute;left:84px;top:250px;color:var(--navy);background:rgba(255,255,255,.6)}
.hero-waves{position:absolute;left:0;bottom:0}

/* gdpr */
.gdpr{top:320px;height:250px;background:var(--navy)}
.gdpr-art{position:absolute;left:100px;top:14px;width:222px;height:222px;border-radius:50%;border:2px dashed rgba(255,255,255,.8);background:radial-gradient(circle,#3fa6e0 0%,#2a56c0 45%,var(--navy) 75%)}
.gdpr-copy{position:absolute;left:401px;top:20px;width:260px;color:var(--white)}
.gdpr-copy h2{font-size:16px;font-weight:600;margin-bottom:12px}
.gdpr-copy p{font-size:9.5px;line-height:13px;margin-bottom:11px}
.gdpr-copy p.small{font-size:8px;line-height:11.5px}
.btn-solid{display:inline-block;background:var(--white);color:var(--navy);font-size:7px;font-weight:500;padding:6px 16px;text-decoration:none;margin-top:4px}

/* services */
.services{top:570px;height:230px;display:flex}
.service{position:relative;width:369px;height:230px;color:var(--white)}
.service-audit{background:linear-gradient(135deg,#3b4a63 0%,#6d7a8f 50%,#a8b2c0 100%)}
.service-legal{background:linear-gradient(135deg,#f2c36b 0%,#8a5a33 40%,#2d2a2e 100%)}
.service h3{position:absolute;left:24px;font-size:15px;font-weight:600}
.service-audit h3{top:88px}
.service-legal h3{top:192px}
.service p{position:absolute;left:24px;top:114px;width:300px;font-size:8px;line-height:11px}
.read-more{position:absolute;left:24px;top:178px;font-size:7px;font-weight:500;color:var(--white);text-decoration:none;border-bottom:1px solid var(--white);padding-bottom:3px}

/* dpo design */
.dpo{top:800px;height:270px;background:var(--slate)}
.dpo-art{position:absolute;left:430px;top:28px;width:308px;height:242px;border-radius:140px 0 0 40px;background:linear-gradient(120deg,#ffe014 0%,#f8d400 100%)}
.dpo-copy{position:absolute;left:84px;top:44px;color:var(--white)}
.dpo-copy h2{font-size:16px;font-weight:500;margin-bottom:3px}
.dpo-copy p{font-size:8px}
.ticks{list-style:none;margin-top:12px}
.ticks li{font-size:9px;display:flex;align-items:center;gap:6px;margin-bottom:4px}
.dpo .btn-outline{margin-top:14px;color:var(--white)}
.dpo-waves{position:absolute;left:0;bottom:0}

/* footer */
.site-footer{top:1070px;height:130px;background:var(--footer);color:var(--white)}
.col{position:absolute;top:10px}
.col h4{font-size:8px;font-weight:500;margin-bottom:6px}
.col a{display:block;font-size:6.5px;color:var(--footer-text);text-decoration:none;line-height:11px}
.col a.is-current{color:var(--yellow)}
.col-brand{left:84px}.col-services{left:261px}.col-connect{left:438px}
.subscribe{width:216px;height:20px;border:1px solid #566272;display:flex;align-items:center;justify-content:space-between;padding:0 10px;font-size:6.5px;color:var(--footer-text)}
.subscribe span.arrow{color:var(--yellow);font-size:9px}
.socials{display:flex;gap:6px;margin-top:10px}
.socials span{width:14px;height:14px;border-radius:50%;background:#5c6878}
.to-top{position:absolute;left:708px;top:10px;font-size:11px;color:var(--white)}
.legal-row{position:absolute;top:114px;font-size:6.5px;color:var(--footer-text)}
.legal-row.copy{left:84px}
.legal-row.links{left:438px}
</style>
</head>
<body>
<div class="page">

  <section class="hero">
    <div class="hero-photo" role="img" aria-label="Photo of hands typing on a laptop in a bright office"></div>
    <div class="brand"><span class="brand-dot"></span><span class="brand-name">KTV</span></div>
    <nav class="nav">
      <a class="is-active" style="left:319px" href="#">HOME</a>
      <a style="left:363px" href="#">ABOUT US</a>
      <a style="left:422px" href="#">OUR SERVICES</a>
      <a style="left:498px" href="#">CASE STUDIES</a>
      <a style="left:573px" href="#">CARRIER</a>
      <a class="btn-contact" href="#">CONTACT US</a>
    </nav>
    <h1 class="hero-copy">We contribute to <strong>bringing Artificial Intelligence and Data-Driven Mind-sets</strong> in enterprises.</h1>
    <a class="btn-outline" href="#">CONSULT NOW</a>
    <svg class="hero-waves" width="738" height="120" viewBox="0 0 738 120">
      <path d="M0 95 C60 60 120 50 190 80 C250 105 300 40 380 70 C450 95 510 60 560 70 C620 85 680 60 738 75 V120 H0Z" fill="#aab4e0" opacity=".7"/>
      <path d="M0 100 C80 95 180 110 260 70 C300 20 330 5 360 40 C400 95 450 90 520 60 C580 35 620 30 660 50 C700 70 720 60 738 55 V120 H0Z" fill="#3a4fb8"/>
      <path d="M0 110 C120 100 240 115 360 95 C480 80 600 100 738 90 V120 H0Z" fill="#0b1a8f"/>
    </svg>
  </section>

  <section class="gdpr">
    <div class="gdpr-art" role="img" aria-label="Illustration of a padlock surrounded by devices and circuit lines"></div>
    <div class="gdpr-copy">
      <h2>What is the GDPR?</h2>
      <p>The General Data Protection Regulation (GDPR) represents the most significant legislative change in 20 years.</p>
      <p class="small">Directly applicable in the 31 countries of the European Economic Area (the 28 Member States of the European Union (EU) and three of the four Member States of the European Free Trade Association), it is imposed in an identical way everywhere and without intervention of each Member ...</p>
      <a class="btn-solid" href="#">EXPLORE MORE</a>
    </div>
  </section>

  <section class="services">
    <article class="service service-audit" role="img" aria-label="Photo of a consultant reviewing documents">
      <h3>Audits &amp; Consultancy</h3>
      <p>The reporting obligations to the supervisory authorities are abolished as of 25 May 2018. They are replaced by compliance and liability requirements and are accompanied by (very) heavy dissuasive</p>
      <a class="read-more" href="#">READ MORE &rarr;</a>
    </article>
    <article class="service service-legal" role="img" aria-label="Photo of a judge's gavel resting on a keyboard">
      <h3>GDPR Legal Advice</h3>
    </article>
  </section>

  <section class="dpo">
    <div class="dpo-art" role="img" aria-label="Illustration of a head in profile with an AI chip and circuit lines"></div>
    <div class="dpo-copy">
      <h2>DPD/DPO Design</h2>
      <p>The original approach is based on 3 foundations:</p>
      <ul class="ticks">
        <li><svg width="8" height="6" viewBox="0 0 8 6"><path d="M1 3l2 2 4-4" stroke="#fff" fill="none" stroke-width="1.2"/></svg>Legal &amp; IT Design</li>
        <li><svg width="8" height="6" viewBox="0 0 8 6"><path d="M1 3l2 2 4-4" stroke="#fff" fill="none" stroke-width="1.2"/></svg>Artificial Intelligence or "AI</li>
        <li><svg width="8" height="6" viewBox="0 0 8 6"><path d="M1 3l2 2 4-4" stroke="#fff" fill="none" stroke-width="1.2"/></svg>Ethics and Human by Design</li>
      </ul>
      <a class="btn-outline" href="#">EXPLORE MORE</a>
    </div>
    <svg class="dpo-waves" width="738" height="76" viewBox="0 0 738 76">
      <path d="M0 45 C40 30 80 10 120 40 C150 62 170 28 210 16 C250 6 270 34 310 30 C360 24 400 6 450 20 C520 38 600 24 660 34 C700 40 720 28 738 24 V76 H0Z" fill="#6e7a87"/>
      <path d="M0 70 C30 62 40 42 70 48 C110 58 140 22 190 14 C230 8 250 42 300 48 C360 55 400 38 450 42 C520 46 560 28 620 32 C680 36 710 42 738 38 V76 H0Z" fill="#3c4758"/>
    </svg>
  </section>

  <footer class="site-footer">
    <div class="col col-brand">
      <h4>KTV</h4>
      <a href="#">About Us</a>
      <a class="is-current" href="#">Case Studies</a>
      <a href="#">Press releases</a>
      <a href="#">Newsletters</a>
      <a href="#">Carrier</a>
      <a href="#">Contact Us</a>
      <a href="#">Sitemap</a>
    </div>
    <div class="col col-services">
      <h4>Services</h4>
      <a href="#">Audit &amp; Assurance</a>
      <a href="#">Financial Advisory</a>
      <a href="#">Legal</a>
      <a href="#">Risk Advisory</a>
      <a href="#">Tax</a>
      <a href="#">Consulting</a>
      <a href="#">All services</a>
    </div>
    <div class="col col-connect">
      <h4>Get Connected</h4>
      <div class="subscribe"><span>Enter your email</span><span class="arrow">&rarr;</span></div>
      <div class="socials"><span></span><span></span><span></span></div>
    </div>
    <span class="to-top">&uarr;</span>
    <p class="legal-row copy">© 2018 KTV.</p>
    <p class="legal-row links">Privacy Policy &nbsp;•&nbsp; Terms of Use &nbsp;•&nbsp; Cookies</p>
  </footer>

</div>
</body>
</html>
```